Homepage Header Image Redesign

We need an image redesign to be used for our Header image on the homepage. We'd like to incorporate the Rocket but it needs to look great on Desktop and mobile.

Here is the homepage: https://brightharbor.com/

You will notice the rocket and how it is being used. When the page scrolls, the rocket appears to be taking off. We would like to see a design that also incorporates our brand's color scheme. The concept can be the same however we would like it to be better. The image needs to fit correctly in our header.

Since we are going to have copy in middle of the screen we need to be creative with how we angle the rocketship. An idea of this is to have the ship fly diagonally from the left towards the top at a 45-degree angle. Also open to playing with rocket placement.

The current Rocket has red fins, but we would like the new rocket to have blue and/or green fins to match the color scheme of our brand.

Design ideas:
Perhaps more detailed rocket and sky with a city in the backdrop.
Perhaps more detailed rocket and sky with Downtown San Diegos city skyline in the backdrop

Open to new ideas as well. We would like to promote creative freedom!

```html
<!DOCTYPE html>
<html lang="en">
<head>
<meta charset="utf-8">
<title>Accessible and Accountable</title>
<link rel="stylesheet" href="https://fonts.googleapis.com/css2?family=Gelasio:wght@700&family=Open+Sans:wght@300&family=Poppins:wght@800&display=swap">
<style>
  :root {
    --bg-start: #16054d;
    --bg-mid: #33075a;
    --bg-end: #4a1090;
    --text-light: #ffffff;
    --button-start: #26f0ff;
    --button-mid: #5a79e0;
    --button-end: #7d1bcc;
    --rocket-light: #d9cdf0;
    --rocket-mid: #8a5bd8;
    --rocket-glow: rgba(140, 40, 200, 0.35);
  }
  * { margin: 0; padding: 0; box-sizing: border-box; }
  html, body {
    width: 1200px;
    height: 745px;
    overflow: hidden;
  }
  .header-hero {
    position: relative;
    width: 1200px;
    height: 745px;
    background: linear-gradient(135deg, var(--bg-start) 0%, var(--bg-mid) 50%, var(--bg-end) 100%);
    overflow: hidden;
  }
  .rocket-illustration {
    position: absolute;
    left: 505px;
    top: 74px;
    width: 180px;
    height: 344px;
    border-radius: 50% 50% 45% 45% / 30% 30% 25% 25%;
    background:
      radial-gradient(ellipse at 50% 85%, rgba(240, 232, 250, 0.9) 0%, rgba(240, 232, 250, 0) 35%),
      radial-gradient(ellipse at 50% 40%, var(--rocket-light) 0%, var(--rocket-mid) 45%, var(--rocket-glow) 70%, rgba(140, 40, 200, 0) 100%);
  }
  .headline {
    position: absolute;
    left: 0;
    width: 1200px;
    top: 486px;
    text-align: center;
    font-family: "Gelasio", Georgia, serif;
    font-weight: 700;
    font-size: 50px;
    line-height: 64px;
    color: var(--text-light);
    padding-left: 28px;
  }
  .headline .caret {
    font-weight: 400;
    font-family: "Open Sans", Arial, sans-serif;
    font-size: 46px;
  }
  .tagline {
    position: absolute;
    left: 0;
    width: 1200px;
    top: 574px;
    text-align: center;
    font-family: "Open Sans", Arial, sans-serif;
    font-weight: 300;
    font-size: 28px;
    line-height: 40px;
    color: var(--text-light);
    padding-left: 12px;
  }
  .contact-button {
    position: absolute;
    left: 427px;
    top: 619px;
    width: 317px;
    height: 81px;
    border-radius: 41px;
    background: linear-gradient(90deg, var(--button-start) 0%, var(--button-mid) 50%, var(--button-end) 100%);
    color: var(--text-light);
    font-family: "Poppins", Arial, sans-serif;
    font-weight: 800;
    font-size: 42px;
    letter-spacing: -0.5px;
    line-height: 81px;
    text-align: center;
    text-decoration: none;
    padding-left: 6px;
  }
</style>
</head>
<body>
  <header class="header-hero">
    <div class="rocket-illustration" role="img" aria-label="Illustration of a lavender rocket with purple fins and a blue porthole lifting off from a white cloud of smoke"></div>
    <h1 class="headline">Accessible and Accountable<span class="caret">|</span></h1>
    <p class="tagline">Call us today for your free consultation!</p>
    <a class="contact-button" href="#contact">CONTACT US</a>
  </header>
</body>
</html>
```